Cloud Phone Service Brochure

We need a brochure for a Cloud Phone Service offering that we offer in Canada. We're a small company that cares about our client's success and protects their privacy. We would like to see designs that reflect us as a stable, trustworthy company which is also fast moving and leading edge. We see ourselves more like Quenby than Harn. Mosaic Vault has built our logo and business card, and we look forward to moving ahead here. I've attached our Business Card file so you have our logo as well as my own shot at some thoughts about content written as a trifold. That specific content does not need to be used, nor does it need to be a trifold. Those phone pictures are the actual phones we use.

```html
<!DOCTYPE html>
<html lang="en">
<head>
<meta charset="utf-8">
<title>Signal Summit – Cloud Phone Service Brochure</title>
<link rel="stylesheet" href="https://fonts.googleapis.com/css2?family=Oswald:wght@400;600;700&family=Open+Sans:wght@400;600;700&display=swap">
<style>
  :root{
    --blue:#1b8bd6;
    --blue-dark:#1270b3;
    --ink:#2a2e33;
    --body:#4a4f55;
    --paper:#ffffff;
    --paper-shade:#f1f2f4;
    --backdrop:#d9dbde;
    --orange:#f2a43a;
    --brown:#4e3426;
  }
  *{box-sizing:border-box;margin:0;padding:0}
  html,body{width:1200px;height:2190px;overflow:hidden}
  body{background:var(--backdrop);font-family:"Open Sans",Arial,sans-serif;color:var(--body);position:relative}
  .spread{position:absolute;left:30px;width:1140px;height:880px;display:flex;box-shadow:0 10px 30px rgba(0,0,0,.18)}
  .spread--outside{top:130px}
  .spread--inside{top:1150px}
  .panel{position:relative;width:380px;height:880px;background:var(--paper);overflow:hidden}
  .panel + .panel{border-left:1px solid #e4e6e9}
  .photo{position:absolute}
  h3{font-family:"Oswald",Arial,sans-serif;font-weight:700;text-transform:uppercase;color:var(--ink);font-size:19px;line-height:1.1;letter-spacing:.3px}
  h3 .accent{color:var(--blue)}
  .list{list-style:none;font-size:13px;line-height:1.5;color:var(--body)}
  .list li{position:relative;padding-left:18px}
  .list li::before{content:"";position:absolute;left:0;top:6px;width:8px;height:8px;border:2px solid var(--blue);border-radius:1px}
  .list .sub{padding-left:34px}
  .list .sub::before{left:18px;border-radius:50%;width:7px;height:7px}
  .brand{display:flex;align-items:center;gap:8px}
  .brand-square{width:26px;height:26px;background:var(--blue)}
  .brand-name{font-family:"Oswald",Arial,sans-serif;font-weight:600;font-size:20px;color:var(--ink);text-transform:uppercase;letter-spacing:1px}

  /* outside: partners panel */
  .partners-photo{left:0;top:0;width:380px;height:230px;background:linear-gradient(135deg,#1c1e22,#3b4048 60%,#6d7580);border-bottom-right-radius:90px}
  .partners-curve{position:absolute;left:0;top:0}
  .partners{position:absolute;left:40px;top:280px;right:40px}
  .badges{display:grid;grid-template-columns:repeat(3,1fr);gap:12px;margin:16px 0 34px}
  .badge{height:34px;background:var(--paper-shade);border:1px solid #d3d6da;border-radius:4px}
  .partners h3{margin-top:18px;margin-bottom:8px}

  /* outside: back panel */
  .contact{position:absolute;left:0;right:0;top:420px;text-align:center}
  .contact .brand{justify-content:center;margin-bottom:26px}
  .contact p{font-size:15px;line-height:1.55;color:var(--ink)}
  .contact .icon{display:block;margin:12px auto 4px}

  /* outside: cover */
  .cover-photo{left:0;top:0;width:380px;height:520px;background:radial-gradient(circle at 60% 55%,var(--orange) 0,#b9712c 18%,var(--brown) 45%,#2c1e17 100%)}
  .cover-frame{position:absolute;left:0;top:0}
  .cover-copy{position:absolute;left:40px;right:40px;top:560px}
  .cover-copy .brand{margin-bottom:22px}
  .headline{font-family:"Oswald",Arial,sans-serif;font-weight:700;font-size:46px;line-height:1;color:var(--ink);text-transform:uppercase}
  .subline{font-family:"Oswald",Arial,sans-serif;font-weight:400;font-size:32px;line-height:1.1;color:var(--blue);text-transform:uppercase;margin-top:4px}
  .cover-url{position:absolute;left:0;right:0;bottom:0;height:70px;background:var(--blue);color:#fff;font-size:17px;letter-spacing:2px;display:flex;align-items:center;justify-content:center}

  /* inside */
  .room-photo{left:0;top:0;width:380px;height:220px;background:linear-gradient(180deg,#eef3f7,#c9d6e0 70%,#9fb2c2);border-bottom-right-radius:80px;border-bottom:8px solid var(--blue)}
  .col{position:absolute;left:36px;right:36px}
  .col h3{margin-bottom:8px}
  .col .list + h3{margin-top:22px}
  .conf-phone{right:40px;bottom:34px;width:90px;height:40px;background:linear-gradient(180deg,#555a60,#1f2226);border-radius:50% 50% 8px 8px}
  .desk-phone{right:30px;top:36px;width:110px;height:80px;background:linear-gradient(160deg,#3a3e44,#111316);border-radius:8px}
  .globe-photo{left:0;bottom:0;width:380px;height:300px;background:radial-gradient(circle at 40% 55%,#8ea6bb 0,#3e5670 30%,#15233a 70%,#0b1422);border-top-left-radius:90px;border-top:8px solid var(--blue)}
</style>
</head>
<body>

<section class="spread spread--outside">
  <article class="panel panel--partners">
    <div class="photo partners-photo" role="img" aria-label="Photo of the desk phones used by the service"></div>
    <svg class="partners-curve" width="380" height="250" aria-hidden="true"><path d="M380 0 V150 Q370 230 290 238 H0" fill="none" stroke="#1b8bd6" stroke-width="8"/></svg>
    <div class="partners">
      <h3>Our <span class="accent">Partners</span></h3>
      <div class="badges">
        <span class="badge"></span><span class="badge"></span><span class="badge"></span>
        <span class="badge"></span><span class="badge"></span><span class="badge"></span>
        <span class="badge"></span><span class="badge"></span><span class="badge"></span>
      </div>
      <h3>We <span class="accent">Are</span></h3>
      <ul class="list">
        <li>70% Renewable Energy</li>
        <li>100% Renewable for 2020</li>
      </ul>
      <h3>We give our time and <span class="accent">skills to help</span></h3>
      <ul class="list">
        <li>Schools</li>
        <li>Community Associations</li>
        <li>Non-profits</li>
        <li>Renewable Energy Initiatives</li>
      </ul>
    </div>
  </article>

  <article class="panel panel--back">
    <div class="contact">
      <div class="brand"><span class="brand-square"></span><span class="brand-name">Signal Summit</span></div>
      <svg class="icon" width="20" height="20" viewBox="0 0 24 24" aria-hidden="true"><path fill="#1b8bd6" d="M6.6 10.8a15 15 0 0 0 6.6 6.6l2.2-2.2c.3-.3.7-.4 1-.2 1.1.4 2.3.6 3.6.6.6 0 1 .4 1 1V20c0 .6-.4 1-1 1C10.6 21 3 13.4 3 4c0-.6.4-1 1-1h3.5c.6 0 1 .4 1 1 0 1.3.2 2.5.6 3.6.1.3 0 .7-.2 1z"/></svg>
      <p>(555)010-4477</p>
      <svg class="icon" width="20" height="20" viewBox="0 0 24 24" aria-hidden="true"><circle cx="12" cy="12" r="9" fill="none" stroke="#1b8bd6" stroke-width="2"/><path d="M3 12h18M12 3c3 3 3 15 0 18M12 3c-3 3-3 15 0 18" fill="none" stroke="#1b8bd6" stroke-width="1.6"/></svg>
      <p>www.signalsummit.example</p>
      <svg class="icon" width="20" height="22" viewBox="0 0 24 26" aria-hidden="true"><path fill="#1b8bd6" d="M12 1a8 8 0 0 0-8 8c0 6 8 16 8 16s8-10 8-16a8 8 0 0 0-8-8zm0 11a3 3 0 1 1 0-6 3 3 0 0 1 0 6z"/></svg>
      <p>PO Box 10482<br>14-2210 Harbour Ridge Road NW<br>Westbrook, Alberta T0X 0X0<br>Canada</p>
    </div>
  </article>

  <article class="panel panel--cover">
    <div class="photo cover-photo" role="img" aria-label="Photo of open hands holding glowing cloud and device icons"></div>
    <svg class="cover-frame" width="380" height="880" aria-hidden="true">
      <polygon points="0,560 100,440 380,440 380,880 0,880" fill="#1b8bd6"/>
      <polygon points="26,572 112,466 380,466 380,810 26,810" fill="#ffffff"/>
    </svg>
    <div class="cover-copy">
      <div class="brand"><span class="brand-square"></span><span class="brand-name">Signal Summit</span></div>
      <div class="headline">Get Connected</div>
      <div class="subline">Anywhere Anytime!</div>
    </div>
    <div class="cover-url">www.signalsummit.example</div>
  </article>
</section>

<section class="spread spread--inside">
  <article class="panel panel--why">
    <div class="photo room-photo" role="img" aria-label="Photo of a video conference room with a wall screen"></div>
    <div class="col" style="top:250px">
      <h3>Why Cloud <span class="accent">Service?</span></h3>
      <ul class="list">
        <li>Cloud Phones mean no setup costs and no hardware to purchase or support.</li>
        <li>Cloud service also offers seamless remote working and multi-office collaboration.</li>
      </ul>
      <h3>Why Signal <span class="accent">Summit?</span></h3>
      <ul class="list">
        <li>Signal Summit believes in building long term collaborative relationships.</li>
        <li>We care about your business as if it was our own.</li>
        <li>Your privacy matters to us. We do not sell, rent or share your data.</li>
      </ul>
      <h3>Phone <br><span class="accent">Service Features:</span></h3>
      <ul class="list">
        <li>All features and functions included</li>
        <li>Conference line included</li>
        <li>Toll Free Number included</li>
        <li>North American LD included</li>
        <li>Monthly billing with no contract</li>
        <li>No hardware or installation costs</li>
        <li>Any high speed internet service</li>
        <li>Keep your existing phone number</li>
        <li>Voicemail to email</li>
        <li>Find Me &amp; Follow Me</li>
        <li>Call Recording</li>
      </ul>
    </div>
    <div class="photo conf-phone" role="img" aria-label="Photo of a conference speakerphone"></div>
  </article>

  <article class="panel panel--video">
    <div class="col" style="top:40px">
      <h3>Video Conferencing <br><span class="accent">Room Configuration</span></h3>
      <ul class="list">
        <li>120 Simultaneous video streams supported</li>
        <li>Most conference sources</li>
        <li class="sub">Video Conf Room System</li>
        <li class="sub">Video Phones</li>
        <li class="sub">Desktop &amp; Laptop Computers</li>
        <li class="sub">Mobile &amp; Tablet Devices</li>
        <li class="sub">SIP PBXes</li>
        <li class="sub">PSTN Phones</li>
        <li>Connect Streaming &amp; Social Live</li>
        <li>1080p HD at 30 fps</li>
        <li>Multi-location conferencing</li>
        <li>Meeting Controls</li>
        <li>Screen Sharing</li>
        <li>Customizable Registration options</li>
        <li>Email Follow-up options</li>
        <li>10 simultaneous sessions</li>
        <li>Encrypted connections</li>
      </ul>
      <h3>IP Video <span class="accent">Telephony</span></h3>
      <ul class="list">
        <li>HD Speakerphone</li>
        <li>HD Video</li>
        <li>7" Touch screen</li>
        <li>Supports Bluetooth Headsets</li>
        <li>Built in camera &amp; privacy shutter</li>
        <li>7-way video conferences on device</li>
        <li>Fully interoperable with our other phone services</li>
        <li>Ideal for remote workers</li>
        <li>Any high-speed internet service</li>
        <li>Video Conference Room solutions available</li>
      </ul>
    </div>
  </article>

  <article class="panel panel--services">
    <div class="photo desk-phone" role="img" aria-label="Photo of an office desk phone"></div>
    <div class="col" style="top:40px">
      <h3>Our <span class="accent">Services</span></h3>
      <ul class="list" style="margin-top:14px">
        <li>Network Support</li>
        <li>Phone Service</li>
        <li>Disaster Recovery</li>
        <li>Remote Backups</li>
        <li>Email Archiving</li>
        <li>Office &amp; Productivity Apps</li>
        <li>Migration Services</li>
        <li>Spam and Virus Filtering</li>
        <li>Server and Network Monitoring</li>
        <li>Printing, Scanning and Plotting</li>
        <li>Firewalls and Security</li>
        <li>Network Design and Planning</li>
        <li>Network and Electrical Cabling</li>
        <li>Wireless coverage planning</li>
        <li>Security cameras &amp; Access Control</li>
      </ul>
    </div>
    <div class="photo globe-photo" role="img" aria-label="Photo of a hand holding a globe made of media screens"></div>
  </article>
</section>

</body>
</html>
```